Need pocket folder design that would multiple technical product pages

Need to design a brochure for an upcoming international exhibition. The company has multiple product types, each product type need one page to capture the technical details. The typical bound brochures are becoming very large and bulky for visitors to carry.

Below link shows the current version of the brochure that was spiral bound.
http://www.brevanjoint.example/sites/default/files/PDF/final_catalogue_1.pdf

I need to graphically design a pocket folder that can hold multiple individual product technical information pages.

This product is typically used for connecting two shafts like a motor and pump. Typical customer is either OEM or local distributors. Visit www.brevanjoint.example for more information
Updates

Industry/Entity Type

Mechanical Engineering

Font styles to use
Serif

Requirements
Must have
• Use of Company logo, company profile.
• We prefer the colors used for the logo.
• Please use uploaded photos on 23 Feb instead of the photos shown on cover.

```html
<!DOCTYPE html>
<html lang="en">
<head>
<meta charset="utf-8">
<title>Brevan Flexible Couplings – Pocket Folder Inside Spread</title>
<link rel="stylesheet" href="https://fonts.googleapis.com/css2?family=Bitter:wght@700&display=swap">
<style>
  :root {
    --backdrop: #e4e4e2;
    --board-dark: #2f3031;
    --board-mid: #4a4b4c;
    --pocket-blue: #4a87d0;
    --pocket-blue-light: #6aa6e6;
    --card-white: #e9edf3;
    --brand-blue: #3a6fb8;
    --pocket-type: #d6e5f7;
    --spine-line: #1f2021;
  }
  html, body {
    margin: 0;
    padding: 0;
    width: 1200px;
    height: 789px;
    overflow: hidden;
    background: var(--backdrop);
  }
  .folder-spread {
    display: block;
    width: 1200px;
    height: 789px;
  }
  .brand-name {
    font-family: "Bitter", Georgia, serif;
    font-weight: 700;
    text-transform: uppercase;
  }
  .card-name {
    font-size: 10px;
    letter-spacing: 0.5px;
    fill: var(--brand-blue);
  }
  .pocket-name {
    font-size: 21px;
    letter-spacing: 2px;
    fill: var(--pocket-type);
  }
</style>
</head>
<body>
<svg class="folder-spread" viewBox="0 0 1200 789" xmlns="http://www.w3.org/2000/svg" aria-label="Open pocket folder, inside spread">
  <defs>
    <radialGradient id="board-texture" cx="50%" cy="35%" r="75%">
      <stop offset="0" stop-color="var(--board-mid)"/>
      <stop offset="1" stop-color="var(--board-dark)"/>
    </radialGradient>
    <radialGradient id="pocket-glow" cx="45%" cy="30%" r="80%">
      <stop offset="0" stop-color="var(--pocket-blue-light)"/>
      <stop offset="1" stop-color="var(--pocket-blue)"/>
    </radialGradient>
  </defs>

  <!-- inside panels -->
  <g class="inside-panels">
    <rect class="panel-left" x="100" y="45" width="500" height="700" fill="url(#board-texture)"/>
    <rect class="panel-right" x="600" y="45" width="500" height="700" fill="url(#board-texture)"/>
    <line class="spine" x1="600" y1="45" x2="600" y2="745" stroke="var(--spine-line)" stroke-width="2"/>
  </g>

  <!-- left pocket with business card slot -->
  <g class="pocket-left">
    <path d="M100,485 H510 Q575,485 575,550 V745 H100 Z" fill="url(#pocket-glow)"/>
    <g class="business-card">
      <rect x="185" y="550" width="205" height="120" fill="var(--card-white)"/>
      <path d="M185,562 L197,550" stroke="#ffffff" stroke-width="3"/>
      <path d="M378,670 L390,658" stroke="#ffffff" stroke-width="3"/>
      <circle cx="287" cy="596" r="9" fill="var(--brand-blue)"/>
      <text class="brand-name card-name" x="287.5" y="624" text-anchor="middle">Brevan Flexible Couplings</text>
    </g>
  </g>

  <!-- right pocket with brand name -->
  <g class="pocket-right">
    <path d="M625,745 V565 Q625,505 685,505 H1100 V745 Z" fill="url(#pocket-glow)"/>
    <circle cx="862" cy="600" r="26" fill="var(--pocket-type)"/>
    <text class="brand-name pocket-name" x="862" y="672" text-anchor="middle">Brevan Flexible Couplings</text>
  </g>
</svg>
</body>
</html>
```